81M business card

I need a business card for a life sciences consulting firm I started. The company name is 81M and the logo is attached. I am looking for something edgey and current but different from the blah standard business card.

Industry/Entity Type

Business

Requirements
Nice to have
• Both sides

```html
<!DOCTYPE html>
<html lang="en">
<head>
<meta charset="utf-8">
<title>81M business card</title>
<link rel="stylesheet" href="https://fonts.googleapis.com/css2?family=Arimo:wght@400;700&family=Open+Sans:wght@300;400&display=swap">
<style>
  :root {
    --navy: #1f3b8a;
    --orange: #f47a20;
    --lilac: #8c92c4;
    --grey-text: #8a8a8a;
    --ink: #111111;
    --card-border: #9a9a9a;
    --paper: #ffffff;
  }
  html, body {
    margin: 0;
    padding: 0;
    width: 1200px;
    height: 2487px;
    overflow: hidden;
    background: var(--paper);
  }
  .sheet {
    position: relative;
    width: 1200px;
    height: 2487px;
    font-family: "Arimo", Arial, sans-serif;
    color: var(--ink);
  }
  .card {
    position: absolute;
    left: 2px;
    width: 1192px;
    height: 752px;
    border: 2px solid var(--card-border);
    border-radius: 10px;
    background: var(--paper);
    overflow: hidden;
  }
  .card--front { top: 14px; }
  .card--back { top: 864px; }
  .card--flat { top: 1728px; }

  .brand-name {
    position: absolute;
    margin: 0;
    font-family: "Arimo", Arial, sans-serif;
    font-weight: 700;
    color: var(--navy);
    line-height: 1;
    letter-spacing: 4px;
  }
  .tagline {
    position: absolute;
    margin: 0;
    font-family: "Open Sans", Arial, sans-serif;
    font-weight: 300;
    color: var(--grey-text);
    line-height: 1.15;
  }
  .decor {
    position: absolute;
  }

  /* front */
  .card--front .brand-name { left: 14px; top: 14px; font-size: 210px; }
  .card--front .tagline { left: 584px; top: 250px; font-size: 40px; text-align: right; }
  .card--front .decor { left: -170px; top: 240px; width: 720px; height: 720px; }
  .contact-block {
    position: absolute;
    right: 30px;
    top: 510px;
    text-align: right;
  }
  .person-name { margin: 0; font-size: 38px; font-weight: 700; }
  .person-title { margin: 8px 0 0; font-size: 33px; }
  .contact-line { margin: 0; font-size: 29px; line-height: 1.3; }
  .contact-line--first { margin-top: 30px; }

  /* back */
  .card--back .decor { left: 470px; top: -60px; width: 800px; height: 800px; }
  .card--back .brand-name { left: 130px; top: 200px; font-size: 260px; }
  .address-block {
    position: absolute;
    left: 26px;
    bottom: 18px;
    font-size: 29px;
    line-height: 1.28;
  }
  .address-block p { margin: 0; }
  .address-block .phone { font-weight: 700; margin-top: 8px; }

  /* flat */
  .mark-dot { position: absolute; left: 30px; top: 120px; width: 380px; height: 380px; }
  .card--flat .brand-name { left: 432px; top: 240px; font-size: 180px; }
  .card--flat .tagline { left: 434px; top: 430px; font-size: 37px; }
  .footer-line {
    position: absolute;
    left: 0;
    right: 0;
    top: 712px;
    margin: 0;
    text-align: center;
    font-size: 29px;
    word-spacing: 2px;
  }
  .footer-line span { margin: 0 12px; }
</style>
</head>
<body>
<main class="sheet">

  <section class="card card--front" aria-label="Card front">
    <svg class="decor" viewBox="0 0 720 720" role="img" aria-label="Faint brand symbol decoration">
      <defs>
        <linearGradient id="frontGlow" x1="0" y1="0" x2="1" y2="1">
          <stop offset="0" stop-color="#8c92c4" stop-opacity="0.75"/>
          <stop offset="1" stop-color="#f7b27a" stop-opacity="0.55"/>
        </linearGradient>
      </defs>
      <circle cx="360" cy="360" r="350" fill="url(#frontGlow)"/>
    </svg>
    <h1 class="brand-name">81M</h1>
    <p class="tagline">regulatory consulting and<br>contract services</p>
    <div class="contact-block">
      <p class="person-name">Sample A. Sample</p>
      <p class="person-title">Position title</p>
      <p class="contact-line contact-line--first">555-123-4567</p>
      <p class="contact-line">email@address.com</p>
    </div>
  </section>

  <section class="card card--back" aria-label="Card back">
    <svg class="decor" viewBox="0 0 800 800" role="img" aria-label="Faint brand symbol decoration">
      <defs>
        <linearGradient id="backGlow" x1="0" y1="0" x2="1" y2="1">
          <stop offset="0" stop-color="#c3c6e2" stop-opacity="0.6"/>
          <stop offset="1" stop-color="#fbd3b0" stop-opacity="0.55"/>
        </linearGradient>
      </defs>
      <circle cx="400" cy="400" r="390" fill="url(#backGlow)"/>
    </svg>
    <h2 class="brand-name">81M</h2>
    <div class="address-block">
      <p>123 Main Street</p>
      <p>Larkfield, VA 01010</p>
      <p class="phone">555-123-4567</p>
      <p>www.website.com</p>
    </div>
  </section>

  <section class="card card--flat" aria-label="Single-sided card">
    <svg class="mark-dot" viewBox="0 0 380 380" aria-hidden="true">
      <circle cx="190" cy="190" r="180" fill="var(--navy)"/>
    </svg>
    <h2 class="brand-name">81M</h2>
    <p class="tagline">regulatory consulting and contract services</p>
    <p class="footer-line"><span>123 Main Street Larkfield, Virginia 01010</span><span>555-123-4567</span><span>www.website.com</span></p>
  </section>

</main>
</body>
</html>
```